BPR Business Card

We need a business card that reflect our business, we have put anther business card as an example of what we like but please feel free to do your own thing.

Here are the items to be placed on card

Glen Harwick
Bright Parcel Route
Mobile: 917-555-4862
Office: 516-555-7104
Fax: 866-555-3927
Email: info@brightparcelroute.example
Website: brightparcelroute.example

I have added raw files to upload

Glen Harwick
Bright Parcel Route
Mobile: 917-555-4862
Office: 516-555-7104
Fax: 866-555-3927 

Target Market(s)

Natural product manufactures, and retailers and distributors

Industry/Entity Type

Business

Requirements
Must have
• 1. Logo
2. The colors of the company

```html
<!DOCTYPE html>
<html lang="en">
<head>
<meta charset="utf-8">
<title>BPR Business Card</title>
<link href="https://fonts.googleapis.com/css2?family=Arimo:wght@400;700&family=Tinos:wght@700&display=swap" rel="stylesheet">
<style>
  :root {
    --board: #e4e5e7;
    --green: #6cb000;
    --black: #000000;
    --white: #ffffff;
    --rule: #3a3a3a;
  }
  * { box-sizing: border-box; margin: 0; padding: 0; }
  html, body { width: 1200px; height: 1000px; overflow: hidden; }
  body { background: var(--board); font-family: "Arimo", Arial, sans-serif; position: relative; }

  .guide { position: absolute; border-left: 1px solid var(--rule); border-bottom: 1px solid var(--rule); left: 80px; }
  .side-tag {
    position: absolute; width: 80px; height: 40px; border-radius: 50%;
    background: var(--white); font-size: 9px; color: #222;
    display: flex; align-items: center; justify-content: center;
    transform: rotate(-18deg); letter-spacing: .2px;
  }

  .card { position: absolute; width: 414px; height: 253px; overflow: hidden; }
  .card svg.shapes { position: absolute; inset: 0; }
  .card-light { border: 1px solid #cfcfcf; }

  .person { position: absolute; left: 215px; width: 200px; top: 57px; text-align: center; }
  .person-name { font-family: "Tinos", "Times New Roman", serif; font-weight: 700; font-size: 16px; color: var(--white); letter-spacing: .5px; white-space: nowrap; }
  .person-role { font-size: 11px; margin-top: 2px; }

  .contact { position: absolute; left: 192px; top: 141px; font-size: 9.5px; line-height: 16.6px; white-space: nowrap; }
  .contact-row { display: flex; }
  .contact-label { width: 42px; }
  .contact-bar { width: 9px; }

  .mark-front {
    position: absolute; left: 40px; top: 110px; width: 140px;
    font-weight: 700; font-size: 17px; line-height: 19px; color: var(--black);
    display: flex; align-items: flex-start; gap: 6px;
  }
  .mark-square { width: 12px; height: 12px; background: currentColor; flex: none; margin-top: 3px; }

  .mark-back {
    position: absolute; left: 0; right: 0; top: 108px; text-align: center;
    font-weight: 700; font-size: 28px; line-height: 34px; letter-spacing: .3px; white-space: nowrap;
  }
  .url { position: absolute; left: 0; right: 0; top: 227px; text-align: center; font-size: 10px; }
</style>
</head>
<body>

  <div class="guide" style="top:95px;height:248px;width:967px;"></div>
  <div class="guide" style="top:405px;height:250px;width:967px;"></div>
  <div class="guide" style="top:712px;height:255px;width:967px;"></div>
  <div class="side-tag" style="left:40px;top:58px;">FRONTSIDE</div>
  <div class="side-tag" style="left:40px;top:388px;">BACKSIDE</div>
  <div class="side-tag" style="left:40px;top:694px;">BACKSIDE</div>

  <!-- front, black top -->
  <section class="card card-light" style="left:143px;top:70px;">
    <svg class="shapes" width="414" height="253" viewBox="0 0 414 253">
      <rect width="414" height="253" fill="var(--black)"/>
      <polygon points="0,102 97,58 180,118 180,253 0,253" fill="var(--white)"/>
      <rect x="180" y="125" width="234" height="128" fill="var(--green)"/>
    </svg>
    <div class="mark-front"><span class="mark-square"></span><span>BRIGHT PARCEL ROUTE</span></div>
    <div class="person">
      <div class="person-name">GLEN HARWICK</div>
      <div class="person-role" style="color:var(--green);">President</div>
    </div>
    <div class="contact" style="color:var(--white);">
      <div class="contact-row"><span class="contact-label">Mobile</span><span class="contact-bar">|</span><span>917-555-4862</span></div>
      <div class="contact-row"><span class="contact-label">Office</span><span class="contact-bar">|</span><span>516-555-7104</span></div>
      <div class="contact-row"><span class="contact-label">Fax</span><span class="contact-bar">|</span><span>866-555-3927</span></div>
      <div class="contact-row"><span class="contact-label">Email</span><span class="contact-bar">|</span><span>info@brightparcelroute.example</span></div>
      <div class="contact-row"><span class="contact-label">Website</span><span class="contact-bar">|</span><span>brightparcelroute.example</span></div>
      <div class="contact-row"><span class="contact-label">Address</span><span class="contact-bar">|</span><span>218 Harbor Lane, Oakdale, NY 11769</span></div>
    </div>
  </section>

  <!-- front, green top -->
  <section class="card card-light" style="left:633px;top:73px;">
    <svg class="shapes" width="414" height="253" viewBox="0 0 414 253">
      <rect width="414" height="253" fill="var(--green)"/>
      <polygon points="0,102 97,58 184,118 184,253 0,253" fill="var(--black)"/>
      <polygon points="0,110 97,66 184,126 184,253 0,253" fill="var(--white)"/>
      <rect x="184" y="122" width="230" height="131" fill="var(--black)"/>
    </svg>
    <div class="mark-front" style="top:115px;"><span class="mark-square"></span><span>BRIGHT PARCEL ROUTE</span></div>
    <div class="person">
      <div class="person-name">GLEN HARWICK</div>
      <div class="person-role" style="color:var(--black);">President</div>
    </div>
    <div class="contact" style="color:var(--white);top:142px;">
      <div class="contact-row"><span class="contact-label" style="color:var(--green);">Mobile</span><span class="contact-bar">|</span><span>917-555-4862</span></div>
      <div class="contact-row"><span class="contact-label" style="color:var(--green);">Office</span><span class="contact-bar">|</span><span>516-555-7104</span></div>
      <div class="contact-row"><span class="contact-label" style="color:var(--green);">Fax</span><span class="contact-bar">|</span><span>866-555-3927</span></div>
      <div class="contact-row"><span class="contact-label" style="color:var(--green);">Email</span><span class="contact-bar">|</span><span>info@brightparcelroute.example</span></div>
      <div class="contact-row"><span class="contact-label" style="color:var(--green);">Website</span><span class="contact-bar">|</span><span>brightparcelroute.example</span></div>
      <div class="contact-row"><span class="contact-label" style="color:var(--green);">Address</span><span class="contact-bar">|</span><span>218 Harbor Lane, Oakdale, NY 11769</span></div>
    </div>
  </section>

  <!-- back, solid green -->
  <section class="card" style="left:141px;top:384px;background:var(--green);">
    <div class="mark-back" style="color:var(--white);">BRIGHT PARCEL ROUTE</div>
    <div class="url" style="color:var(--white);">brightparcelroute.example</div>
  </section>

  <!-- back, solid black -->
  <section class="card" style="left:636px;top:385px;background:var(--black);">
    <div class="mark-back" style="color:var(--green);">BRIGHT PARCEL ROUTE</div>
    <div class="url" style="color:var(--green);">brightparcelroute.example</div>
  </section>

  <!-- back, green with white band -->
  <section class="card" style="left:138px;top:689px;">
    <svg class="shapes" width="414" height="253" viewBox="0 0 414 253">
      <rect width="414" height="253" fill="var(--green)"/>
      <polygon points="0,56 240,56 274,84 414,84 414,170 0,191" fill="var(--white)"/>
    </svg>
    <div class="mark-back" style="color:var(--green);top:106px;">BRIGHT PARCEL ROUTE</div>
    <div class="url" style="color:var(--white);top:228px;">brightparcelroute.example</div>
  </section>

  <!-- back, black with white band -->
  <section class="card" style="left:636px;top:689px;">
    <svg class="shapes" width="414" height="253" viewBox="0 0 414 253">
      <rect width="414" height="253" fill="var(--black)"/>
      <polygon points="0,56 240,56 274,84 414,84 414,170 0,191" fill="var(--white)"/>
    </svg>
    <div class="mark-back" style="color:var(--black);top:106px;">BRIGHT PARCEL ROUTE</div>
    <div class="url" style="color:var(--white);top:224px;">brightparcelroute.example</div>
  </section>

</body>
</html>
```